need a clean, modern job advertisement designed for social media (Facebook & Instagram).

The post is to advertise two positions:
• Leading Hand Boilermaker
• Dragline Fitter
We want the design to match our KRT Plant Services branding: blue, white, strong, professional, mining-industry style.
What the design should include:
Bold headline: “WE’RE HIRING”
Sub-headline: “Leading Hand Boilermaker & Dragline Fitter”
Key points:
• Bowen Basin based
• Dragline & shovel maintenance
• Great pay + long-term work
• Locally owned & operated
KRT logo placed cleanly
Space for 1–2 images (boilermaking or dragline work)
Design style:
Strong and industrial
Blue/white colour scheme
Easy to read at a glance
Suitable for a square 1080×1080 design

```html
<!DOCTYPE html>
<html lang="en">
<head>
<meta charset="utf-8">
<title>KRT Plant Services – We're Hiring</title>
<link rel="stylesheet" href="https://fonts.googleapis.com/css2?family=Montserrat:ital,wght@0,900;1,800&family=Oswald:wght@500;600&family=Lato:wght@400&display=swap">
<style>
  :root {
    --page-bg: #f3f3f5;
    --white: #ffffff;
    --navy: #0d2a45;
    --ink: #10223f;
    --blue-deep: #0a56d8;
    --blue-bright: #1f9cf0;
    --sky: #2aa8ee;
    --orange: #f7660f;
    --amber: #fcb313;
    --photo-a: #1b3bd6;
    --photo-b: #2f6cf2;
  }
  html, body {
    margin: 0;
    padding: 0;
    width: 1200px;
    height: 1137px;
    overflow: hidden;
    background: var(--page-bg);
  }
  .ad {
    position: absolute;
    left: 182px;
    top: 136px;
    width: 722px;
    height: 722px;
    transform: scale(1.1846);
    transform-origin: 0 0;
    background: var(--white);
    overflow: hidden;
  }
  .ad-shapes {
    position: absolute;
    inset: 0;
    width: 722px;
    height: 722px;
  }
  .headline {
    position: absolute;
    left: 26px;
    top: 28px;
    margin: 0;
    font-family: "Montserrat", sans-serif;
    font-weight: 900;
    font-size: 67px;
    line-height: 60px;
    letter-spacing: 1px;
    background: linear-gradient(180deg, var(--blue-deep), var(--blue-bright));
    -webkit-background-clip: text;
    background-clip: text;
    color: transparent;
  }
  .roles {
    position: absolute;
    left: 28px;
    top: 166px;
    margin: 0;
    font-family: "Oswald", sans-serif;
    font-weight: 600;
    font-size: 31px;
    line-height: 44px;
    color: var(--ink);
  }
  .roles-rule {
    position: absolute;
    left: 30px;
    top: 266px;
    width: 236px;
    height: 2px;
    background: var(--blue-bright);
  }
  .key-points {
    position: absolute;
    left: 28px;
    top: 284px;
    margin: 0;
    padding: 0;
    list-style: none;
    font-family: "Lato", sans-serif;
    font-size: 24px;
    line-height: 31px;
    color: var(--ink);
  }
  .key-points li {
    position: relative;
    padding-left: 20px;
    max-width: 260px;
  }
  .key-points li::before {
    content: "";
    position: absolute;
    left: 0;
    top: 12px;
    width: 9px;
    height: 9px;
    border-radius: 50%;
    background: var(--orange);
  }
  .perk {
    position: absolute;
    left: 30px;
    width: 108px;
    height: 124px;
    display: flex;
    align-items: center;
    justify-content: center;
    text-align: center;
    font-family: "Oswald", sans-serif;
    font-weight: 500;
    color: var(--ink);
  }
  .perk svg {
    position: absolute;
    inset: 0;
  }
  .perk span { position: relative; }
  .perk-pay { top: 424px; font-size: 27px; line-height: 32px; }
  .perk-term { top: 546px; font-size: 22px; line-height: 25px; }
  .brand {
    position: absolute;
    left: 180px;
    top: 548px;
    width: 240px;
    display: flex;
    align-items: center;
    justify-content: center;
    gap: 10px;
    font-family: "Oswald", sans-serif;
    font-weight: 600;
    font-size: 28px;
    color: var(--white);
  }
  .brand-dot {
    width: 14px;
    height: 14px;
    border-radius: 50%;
    background: var(--sky);
  }
  .tagline {
    position: absolute;
    left: 120px;
    top: 679px;
    width: 360px;
    margin: 0;
    text-align: center;
    font-family: "Montserrat", sans-serif;
    font-style: italic;
    font-weight: 800;
    font-size: 19px;
    color: var(--sky);
  }
</style>
</head>
<body>
  <main class="ad">
    <svg class="ad-shapes" viewBox="0 0 722 722" aria-hidden="false">
      <defs>
        <linearGradient id="photoTone" x1="0" y1="0" x2="1" y2="1">
          <stop offset="0" stop-color="var(--photo-a)"/>
          <stop offset="1" stop-color="var(--photo-b)"/>
        </linearGradient>
      </defs>
      <polygon class="band-amber" points="395,395 440,395 722,677 722,722 395,722" fill="var(--amber)"/>
      <polygon class="band-orange" points="395,330 540,218 585,262 395,460" fill="var(--orange)"/>
      <polygon class="photo-welding" role="img" aria-label="Photo of a boilermaker welding on site"
               points="330,0 722,0 722,70 556,236" fill="url(#photoTone)"/>
      <polygon class="photo-dragline" role="img" aria-label="Photo of fitters working on a dragline"
               points="722,92 572,246 414,404 722,704" fill="url(#photoTone)"/>
      <polyline class="frame-line" points="722,80 565,238" stroke="var(--white)" stroke-width="6" fill="none"/>
      <polyline class="frame-line" points="722,76 562,236" stroke="var(--amber)" stroke-width="2" fill="none"/>
      <polyline class="frame-line" points="722,104 578,248 420,404 722,710" stroke="var(--white)" stroke-width="6" fill="none"/>
      <line class="frame-line" x1="318" y1="0" x2="554" y2="238" stroke="var(--orange)" stroke-width="4"/>
      <polygon class="panel-navy" points="0,722 395,328 608,722" fill="var(--navy)"/>
    </svg>

    <h1 class="headline">WE’RE<br>HIRING</h1>
    <h2 class="roles">Leading Hand Boilermaker<br>&amp; Dragline Fitter</h2>
    <div class="roles-rule"></div>
    <ul class="key-points">
      <li>Bowen Basin based</li>
      <li>Dragline &amp; shovel maintenance</li>
    </ul>

    <div class="perk perk-pay">
      <svg viewBox="0 0 108 124"><polygon points="54,2 106,32 106,92 54,122 2,92 2,32" fill="var(--white)" stroke="var(--sky)" stroke-width="2"/></svg>
      <span>Great<br>Pay!</span>
    </div>
    <div class="perk perk-term">
      <svg viewBox="0 0 108 124"><polygon points="54,2 106,32 106,92 54,122 2,92 2,32" fill="var(--white)" stroke="var(--sky)" stroke-width="2"/></svg>
      <span>Long<br>Term<br>Work</span>
    </div>

    <div class="brand"><span class="brand-dot"></span>KRT Plant Services</div>
    <p class="tagline">Locally owned &amp; operated</p>
  </main>
</body>
</html>
```